Stationery Design Project

I am looking for stationary design for an automotive collision repair company. This needs to work with my business cards just designed here. I've attached. I need 8.5 x 11 stationary and corissponding envelopes. a jot tab note pad also. Our companies focus is very high end customer service driven . Our customer base is 35-65 middle to high income. Please include company name, logo, address, phone number, web address. The business card is two greys with green and white writing. I invision a light grey background with a darker grey band on it that contains the logo.
Updates

I justĀ 

Why is no one touching this project

Target Market(s)

60%. Women 40% men. Age 35-60

Industry/Entity Type

Automotive

Requirements
Must have
• Tie in with business cards. So it needs grey tones with green and white logo. Name, address, phone and web address. Must have 8.5 x 11 paper and envelopes.
Nice to have
• Jot tab notes

```html
<!DOCTYPE html>
<html lang="en">
<head>
<meta charset="utf-8">
<title>Panelcraft Stationery Set</title>
<link href="https://fonts.googleapis.com/css2?family=Roboto:wght@400;900&display=swap" rel="stylesheet">
<style>
  :root {
    --backdrop: #c9cacb;
    --paper: #ffffff;
    --band-dark: #2f2e2c;
    --band-mid: #8a8b8c;
    --card-top: #b9babb;
    --brand-green: #7cc242;
    --text-light: #d8d8d8;
    --shadow: rgba(0,0,0,0.28);
  }
  * { margin: 0; padding: 0; box-sizing: border-box; }
  html, body { width: 811px; height: 1200px; overflow: hidden; }
  body {
    background: var(--backdrop);
    font-family: "Roboto", Arial, sans-serif;
    position: relative;
  }
  .piece {
    position: absolute;
    background: var(--paper);
    box-shadow: 3px 4px 10px var(--shadow);
    overflow: hidden;
  }
  .piece svg.shapes { position: absolute; inset: 0; width: 100%; height: 100%; }
  .brand-name {
    position: absolute;
    font-weight: 900;
    color: var(--brand-green);
    letter-spacing: -0.3px;
    white-space: nowrap;
  }
  .fine {
    position: absolute;
    color: var(--text-light);
    font-size: 5.5px;
    line-height: 1.5;
    white-space: nowrap;
  }

  .letterhead { left: 38px; top: 27px; width: 494px; height: 665px; }
  .letterhead .brand-name { left: 132px; top: 12px; font-size: 19px; }
  .letterhead .address { left: 40px; bottom: 12px; }
  .letterhead .contact { right: 22px; bottom: 26px; text-align: right; }

  .notepad { left: 595px; top: 69px; width: 194px; height: 192px; }
  .notepad .brand-name { left: 62px; top: 11px; font-size: 13px; }

  .business-card { left: 635px; top: 343px; width: 114px; height: 211px; background: var(--band-dark); }
  .business-card .brand-name { left: 22px; top: 50px; font-size: 12px; }
  .business-card .holder { left: 0; right: 0; top: 86px; text-align: center; }
  .business-card .card-foot { left: 0; right: 0; bottom: 12px; text-align: center; }

  .envelope { height: 240px; }
  .envelope-back { left: 40px; top: 770px; width: 735px; }
  .envelope-front { left: 120px; top: 890px; width: 655px; }
  .envelope .brand-name { font-size: 15px; }
  .envelope-back .brand-name { left: 252px; top: 14px; }
  .envelope-front .brand-name { left: 40px; top: 20px; }
  .envelope-front .return { left: 40px; top: 42px; }
</style>
</head>
<body>

<section class="piece letterhead" aria-label="Letterhead">
  <svg class="shapes" viewBox="0 0 494 665" preserveAspectRatio="none">
    <path d="M0 0 H494 V48 C320 48 130 70 0 210 Z" fill="var(--band-mid)"/>
    <path d="M0 0 H494 V40 C320 40 120 60 0 196 Z" fill="var(--band-dark)"/>
    <path d="M494 520 C440 590 330 650 180 665 H494 Z" fill="var(--band-mid)"/>
    <path d="M494 532 C445 600 340 655 200 665 H494 Z" fill="var(--band-dark)"/>
  </svg>
  <div class="brand-name">Panelcraft</div>
  <div class="fine contact">T: 555 014 2280<br>F: 555 014 2281<br>www.panelcraft.com</div>
  <div class="fine address" style="color:#999">1280 Harbor Road, Suite 4, Lakeview</div>
</section>

<section class="piece notepad" aria-label="Jot tab note pad">
  <svg class="shapes" viewBox="0 0 194 192" preserveAspectRatio="none">
    <path d="M0 0 H194 V64 C140 50 70 44 0 50 Z" fill="var(--band-mid)"/>
    <path d="M0 0 H194 V58 C140 44 70 38 0 44 Z" fill="var(--band-dark)"/>
  </svg>
  <div class="brand-name">Panelcraft</div>
</section>

<section class="piece business-card" aria-label="Business card">
  <svg class="shapes" viewBox="0 0 114 211" preserveAspectRatio="none">
    <defs>
      <linearGradient id="card-fade" x1="0" y1="0" x2="0" y2="1">
        <stop offset="0" stop-color="#d6d7d8"/>
        <stop offset="1" stop-color="#7d7e7f"/>
      </linearGradient>
    </defs>
    <path d="M0 0 H114 V42 C80 48 40 50 0 44 Z" fill="url(#card-fade)"/>
  </svg>
  <div class="brand-name">Panelcraft</div>
  <div class="fine holder">Dana Ellis<br>Owner<br>T: 555 014 2280<br>F: 555 014 2281<br>dana@panelcraft.com</div>
  <div class="fine card-foot">1280 Harbor Road, Lakeview<br>www.panelcraft.com</div>
</section>

<section class="piece envelope envelope-back" aria-label="Envelope back">
  <svg class="shapes" viewBox="0 0 735 240" preserveAspectRatio="none">
    <path d="M0 0 H735 V40 C560 40 260 70 0 150 Z" fill="var(--band-mid)"/>
    <path d="M0 0 H735 V32 C560 32 260 60 0 140 Z" fill="var(--band-dark)"/>
  </svg>
  <div class="brand-name">Panelcraft</div>
</section>

<section class="piece envelope envelope-front" aria-label="Envelope front">
  <svg class="shapes" viewBox="0 0 655 240" preserveAspectRatio="none">
    <path d="M0 0 H655 V20 C420 22 200 50 0 140 Z" fill="var(--band-mid)"/>
    <path d="M0 0 H655 V12 C420 14 200 40 0 128 Z" fill="var(--band-dark)"/>
  </svg>
  <div class="brand-name">Panelcraft</div>
  <div class="fine return">1280 Harbor Road, Lakeview<br>www.panelcraft.com</div>
</section>

</body>
</html>
```